Brightwell Conduit Builders needs an ad for Harlow Guild of Merchants

Hello, we need a full page ad for the upcoming 2020 Harlow Guild of Merchants magazine. We need something that shows all of the services we offer as well as the information about our company including website, facebook, and instagram.

Target Market(s)

PIPELINE INDUSTRY

Font styles to use
Serif
Sans Serif

Colors

Designer to choose colors to be used in the design.

Requirements
Must have
• It must include our logo and also our slogan building on integrity.
• Address:
• 4815 N FARM LANE 2290
• Carston, TX 70412
• Office: 312.555.0187
• website: brightwellcbx.example
• facebook: https://www.facebook.com/brightwellconduitbuilders
Nice to have
• Our Services:
• Pipeline:
• Transmission Pipelines
• Gathering / Distribution Pipelines
• Pipeline Integrity
• Pipeline Maintenance
• Pipeline Rehabilitation
• Pre-construction Planning
• Valve Change Outs
• Road / Pad Construction
• Hydrostatic Testing
• Horizontal Directional Drilling
• Right-of-Way:
• Project Management
• Land Owner Relations
• ROW Clearing
• ROW Maintenance
• Line Locating
• GPS Coordinates
• Compressor Stations:
• Construction of Prefabricated Steel Facilities
• Excavation / Grading
• Compressor Installation
• Meter Stations

```html
<!DOCTYPE html>
<html lang="en">
<head>
<meta charset="utf-8">
<title>Brightwell Conduit Builders – Full Page Ad</title>
<link rel="stylesheet" href="https://fonts.googleapis.com/css2?family=Montserrat:wght@300;400;500;600;700;800&display=swap">
<style>
  :root {
    --maroon: #8a1730;
    --ink: #2b2b2b;
    --white: #ffffff;
    --silver-light: #e9e9e9;
    --silver-dark: #b9b9b9;
    --tab-dark: #7a7a7a;
    --tab-light: #bdbdbd;
  }
  * { margin: 0; padding: 0; box-sizing: border-box; }
  html, body { width: 965px; height: 1200px; overflow: hidden; background: var(--white); }
  body { font-family: "Montserrat", sans-serif; color: var(--ink); }
  .ad { position: relative; width: 965px; height: 1200px; background: var(--white); overflow: hidden; }

  .photo { position: absolute; }
  .photo--crew-top {
    left: 0; top: 0; width: 965px; height: 480px;
    background: linear-gradient(160deg, #e8eef2 0%, #cfd6d6 30%, #a89a7a 58%, #8b7d5a 80%, #b9a35a 100%);
  }
  .photo--pipe-fitting {
    left: 512px; top: 640px; width: 453px; height: 325px;
    background: linear-gradient(170deg, #e4e8ec 0%, #b86a3f 28%, #a45a35 55%, #8fb8a3 75%, #a35a35 100%);
  }
  .photo--crew-bottom {
    left: 0; top: 1060px; width: 505px; height: 140px;
    background: linear-gradient(175deg, #d9d6cf 0%, #b06a42 40%, #9a5232 75%, #c07b4f 100%);
  }

  .brand { position: absolute; left: 34px; top: 160px; display: flex; align-items: center; gap: 14px; }
  .brand__mark { width: 56px; height: 56px; border-radius: 50%; background: var(--maroon); }
  .brand__text { display: flex; flex-direction: column; }
  .brand__name { font-size: 22px; font-weight: 600; color: var(--maroon); line-height: 1.1; }
  .brand__tagline { font-size: 11px; font-weight: 500; color: var(--maroon); margin-top: 4px; }

  .headline-panel {
    position: absolute; left: 500px; top: 430px; width: 465px; height: 210px;
    background: var(--white); padding: 36px 0 0 40px;
  }
  .headline__light { font-size: 42px; font-weight: 300; letter-spacing: 1px; color: #444; line-height: 1; }
  .headline__bold { font-size: 62px; font-weight: 800; color: var(--maroon); line-height: 1; letter-spacing: 1px; }
  .headline__sub { margin-top: 14px; font-size: 19px; font-weight: 400; color: #333; line-height: 1.2; letter-spacing: .5px; }
  .headline__pointer { position: absolute; left: 190px; bottom: -1px; width: 26px; height: 14px; }

  .services {
    position: absolute; left: 0; top: 480px; width: 500px; height: 572px;
    background: var(--maroon); color: var(--white);
  }
  .services__tab {
    position: absolute; left: 0; top: 440px; width: 262px; height: 46px;
    background: linear-gradient(90deg, var(--tab-dark), var(--tab-light));
    color: var(--white); font-size: 21px; font-weight: 700;
    padding: 10px 0 0 40px;
    clip-path: polygon(0 0, 100% 0, 92% 100%, 0 100%);
  }
  .service-group { position: absolute; display: flex; align-items: center; }
  .service-group__label { font-size: 19px; font-weight: 700; line-height: 1.2; }
  .service-list { list-style: none; font-size: 15.5px; font-weight: 400; line-height: 1.55; }
  .service-list li::before { content: "+"; font-weight: 700; margin-right: 8px; }

  .group--pipeline { left: 40px; top: 28px; }
  .group--pipeline .service-group__label { width: 160px; }
  .group--row { left: 40px; top: 285px; }
  .group--row .service-list { width: 230px; }
  .group--compressor { left: 40px; top: 470px; }
  .group--compressor .service-group__label { width: 160px; }

  .divider { position: absolute; left: 40px; width: 420px; height: 1px; background: rgba(255,255,255,.55); }
  .divider--one { top: 268px; }
  .divider--two { top: 455px; }

  .contact {
    position: absolute; left: 512px; top: 975px; width: 453px; height: 150px;
    background: linear-gradient(120deg, var(--silver-light), var(--silver-dark));
    padding: 20px 24px 0 34px; color: #333;
  }
  .contact__row { display: flex; align-items: flex-start; gap: 12px; margin-bottom: 10px; }
  .contact__icon { width: 14px; height: 14px; flex: none; margin-top: 3px; }
  .contact__address { font-size: 15px; line-height: 1.25; text-transform: uppercase; }
  .contact__phone { font-size: 22px; font-weight: 700; letter-spacing: .5px; }
  .contact__web { font-size: 17px; }
  .contact__web strong { font-weight: 700; }
  .social { position: absolute; right: 24px; top: 60px; display: flex; gap: 8px; }
  .social__dot { width: 26px; height: 26px; border-radius: 50%; background: var(--maroon); }
</style>
</head>
<body>
<main class="ad">
  <div class="photo photo--crew-top" role="img" aria-label="Pipeline crew in hard hats and safety vests welding pipe on a dusty right-of-way"></div>

  <div class="brand">
    <div class="brand__mark"></div>
    <div class="brand__text">
      <span class="brand__name">Brightwell Conduit Builders</span>
      <span class="brand__tagline">Building on Integrity</span>
    </div>
  </div>

  <div class="services__tab">Our Services:</div>

  <section class="services">
    <div class="service-group group--pipeline">
      <h3 class="service-group__label">Pipeline:</h3>
      <ul class="service-list">
        <li>Transmission Pipelines</li>
        <li>Gathering / Distribution Pipelines</li>
        <li>Pipeline Integrity</li>
        <li>Pipeline Maintenance</li>
        <li>Pipeline Rehabilitation</li>
        <li>Pre-construction Planning</li>
        <li>Valve Change Outs</li>
        <li>Road / Pad Construction</li>
        <li>Hydrostatic Testing</li>
        <li>Horizontal Directional Drilling</li>
      </ul>
    </div>
    <div class="divider divider--one"></div>
    <div class="service-group group--row">
      <ul class="service-list">
        <li>Project Management</li>
        <li>Land Owner Relations</li>
        <li>ROW Clearing</li>
        <li>ROW Maintenance</li>
        <li>Line Locating</li>
        <li>GPS Coordinates</li>
      </ul>
      <h3 class="service-group__label">Right-of-Way:</h3>
    </div>
    <div class="divider divider--two"></div>
    <div class="service-group group--compressor">
      <h3 class="service-group__label">Compressor<br>Stations:</h3>
      <ul class="service-list">
        <li>Excavation / Grading</li>
        <li>Compressor Installation</li>
        <li>Meter Stations</li>
      </ul>
    </div>
  </section>

  <section class="headline-panel">
    <h1>
      <span class="headline__light">BUILDING ON</span><br>
      <span class="headline__bold">INTEGRITY</span>
    </h1>
    <p class="headline__sub">OUR GOAL IS TO MAKE SURE<br>YOUR NEEDS ARE MET.</p>
    <svg class="headline__pointer" viewBox="0 0 26 14"><polygon points="0,14 13,0 26,14" fill="#e4e8ec"/></svg>
  </section>

  <div class="photo photo--pipe-fitting" role="img" aria-label="Two workers in hard hats grinding a weld on a green coated pipeline over red soil"></div>
  <div class="photo photo--crew-bottom" role="img" aria-label="Crew lowering a section of pipe at a compressor station site"></div>

  <section class="contact">
    <div class="contact__row">
      <svg class="contact__icon" viewBox="0 0 14 14"><path d="M7 0a5 5 0 0 0-5 5c0 3.5 5 9 5 9s5-5.5 5-9a5 5 0 0 0-5-5zm0 7a2 2 0 1 1 0-4 2 2 0 0 1 0 4z" fill="#8a1730"/></svg>
      <p class="contact__address">4815 N Farm Lane 2290 Carston,<br>TX 70412</p>
    </div>
    <div class="contact__row">
      <svg class="contact__icon" viewBox="0 0 14 14"><path d="M3 1l2 0 1 3-1.5 1.2a8 8 0 0 0 4.3 4.3L10 8l3 1v2c0 1-1 2-2 2C5.5 13 1 8.5 1 3c0-1 1-2 2-2z" fill="#8a1730"/></svg>
      <p class="contact__phone">312.555.0187</p>
    </div>
    <div class="contact__row">
      <svg class="contact__icon" viewBox="0 0 14 14"><circle cx="7" cy="7" r="6" fill="none" stroke="#8a1730" stroke-width="1.5"/><path d="M1 7h12M7 1c-3 3-3 9 0 12M7 1c3 3 3 9 0 12" fill="none" stroke="#8a1730" stroke-width="1.2"/></svg>
      <p class="contact__web">www.<strong>brightwellcbx</strong>.example</p>
    </div>
    <div class="social">
      <span class="social__dot" role="img" aria-label="Social profile link"></span>
      <span class="social__dot" role="img" aria-label="Photo sharing profile link"></span>
    </div>
  </section>
</main>
</body>
</html>
```